KEM Logistics - Banner 2.5' x 8' for 20+ locations

Need a banner designed that will pop. This banner will be displayed at over 20 of our transportation facilities. Goal is for the banner to grab the attention of employees, contractors and clients and help reinforce our mission and core values. Designed needs to include KEM Logo, our core values and mission statement. Red and Black are the main company colors and we need to stay within that theme and color pallet. Attached is a previous version that was too basic and boring. Willing to consider a design that excludes the mission statement.

```html
<!DOCTYPE html>
<html lang="en">
<head>
<meta charset="utf-8">
<title>KEM Logistics – Core Values Banner</title>
<link rel="stylesheet" href="https://fonts.googleapis.com/css2?family=Montserrat:wght@500;600;700&family=Poppins:wght@500;600&display=swap">
<style>
  :root {
    --brand-red: #d02a1d;
    --brand-red-deep: #b81f14;
    --photo-light: #f3c4bd;
    --photo-mid: #e2776b;
    --ink: #262626;
    --icon-ring: #5a5a5a;
    --white: #ffffff;
    --logo-red: #c51f15;
  }
  * { box-sizing: border-box; margin: 0; padding: 0; }
  html, body { width: 1200px; height: 375px; overflow: hidden; background: var(--brand-red); }
  .banner {
    position: relative;
    width: 1200px;
    height: 375px;
    overflow: hidden;
    background: var(--brand-red);
    font-family: "Poppins", "Montserrat", sans-serif;
    color: var(--white);
  }
  .banner__photo {
    position: absolute;
    top: 0; right: 0;
    width: 620px; height: 375px;
    background:
      radial-gradient(ellipse at 75% 30%, var(--photo-light) 0%, transparent 55%),
      radial-gradient(ellipse at 45% 70%, var(--photo-mid) 0%, transparent 60%),
      linear-gradient(100deg, var(--brand-red) 0%, var(--photo-mid) 45%, var(--photo-light) 100%);
    -webkit-mask-image: linear-gradient(90deg, transparent 0%, #000 30%);
            mask-image: linear-gradient(90deg, transparent 0%, #000 30%);
  }
  .banner__url {
    position: absolute;
    top: 13px; right: 33px;
    font-family: "Montserrat", sans-serif;
    font-weight: 700;
    font-size: 12px;
    letter-spacing: 2px;
    color: var(--ink);
  }
  .values {
    position: absolute;
    top: 40px; left: 30px;
    display: grid;
    grid-template-columns: 235px 233px 240px;
    row-gap: 50px;
    list-style: none;
  }
  .value { display: flex; align-items: flex-start; gap: 12px; }
  .value__icon {
    flex: none;
    width: 60px; height: 60px;
    border-radius: 50%;
    background: var(--ink);
    box-shadow: 0 0 0 3px var(--icon-ring);
    display: flex; align-items: center; justify-content: center;
  }
  .value__icon svg { width: 32px; height: 32px; }
  .value__label {
    font-weight: 600;
    font-size: 15px;
    line-height: 20px;
    padding-top: 4px;
  }
  .mission {
    position: absolute;
    top: 260px; left: 0;
    width: 692px;
    text-align: center;
    font-family: "Montserrat", sans-serif;
    font-weight: 500;
    font-size: 17px;
    line-height: 25.5px;
    letter-spacing: 2.2px;
    text-transform: uppercase;
  }
  .brand {
    position: absolute;
    top: 270px; right: 30px;
    display: flex; align-items: center; gap: 10px;
    font-family: "Montserrat", sans-serif;
    font-weight: 700;
    font-size: 30px;
    color: var(--logo-red);
  }
  .brand__dot { width: 18px; height: 18px; border-radius: 50%; background: var(--logo-red); }
</style>
</head>
<body>
<div class="banner">
  <div class="banner__photo" role="img" aria-label="Photo of a toy forklift carrying a fragile box on a laptop keyboard, with a delivery van and an airplane behind, tinted red"></div>

  <div class="banner__url">www.kemlogistics.com</div>

  <ul class="values">
    <li class="value">
      <span class="value__icon"><svg viewBox="0 0 32 32" fill="none" stroke="#fff" stroke-width="2.6" stroke-linejoin="round"><path d="M16 27 L5 16 A6 6 0 0 1 16 8 A6 6 0 0 1 27 16 Z"/></svg></span>
      <span class="value__label">Do the right<br>things for the<br>right reasons</span>
    </li>
    <li class="value">
      <span class="value__icon"><svg viewBox="0 0 32 32" fill="#fff"><rect x="4" y="20" width="6" height="8"/><rect x="13" y="15" width="6" height="13"/><rect x="22" y="11" width="6" height="17"/><path d="M25 2 L31 9 H19 Z"/></svg></span>
      <span class="value__label">Pursue<br>growth and<br>development</span>
    </li>
    <li class="value">
      <span class="value__icon"><svg viewBox="0 0 32 32" fill="none" stroke="#fff" stroke-width="2.4" stroke-linecap="round"><path d="M6 14 A10 10 0 0 1 24 8"/><path d="M26 18 A10 10 0 0 1 8 24"/><path d="M24 3 V8 H19"/><path d="M8 29 V24 H13"/></svg></span>
      <span class="value__label">Build a<br>positive team<br>atmosphere</span>
    </li>
    <li class="value">
      <span class="value__icon"><svg viewBox="0 0 32 32" fill="#fff"><path d="M5 8 l1.2 2.4 2.6.4-1.9 1.8.5 2.6L5 14l-2.4 1.2.5-2.6-1.9-1.8 2.6-.4Z"/><path d="M16 8 l1.2 2.4 2.6.4-1.9 1.8.5 2.6L16 14l-2.4 1.2.5-2.6-1.9-1.8 2.6-.4Z"/><path d="M27 8 l1.2 2.4 2.6.4-1.9 1.8.5 2.6L27 14l-2.4 1.2.5-2.6-1.9-1.8 2.6-.4Z"/><rect x="3" y="21" width="26" height="4" rx="2"/></svg></span>
      <span class="value__label">Deliver<br>WOW through<br>service</span>
    </li>
    <li class="value">
      <span class="value__icon"><svg viewBox="0 0 32 32" fill="none" stroke="#fff" stroke-width="2.4" stroke-linejoin="round" stroke-linecap="round"><path d="M16 3 L27 7 V15 C27 22 22 27 16 29 C10 27 5 22 5 15 V7 Z"/><path d="M11 16 L15 20 L22 12"/></svg></span>
      <span class="value__label">Do<br>everything<br>Safely</span>
    </li>
    <li class="value">
      <span class="value__icon"><svg viewBox="0 0 32 32" fill="#fff"><path d="M16 2 l3.5 9 9.5.6-7.3 6 2.4 9.3L16 21.7 7.9 26.9l2.4-9.3-7.3-6 9.5-.6Z"/></svg></span>
      <span class="value__label">Have<br>Fun</span>
    </li>
  </ul>

  <p class="mission">Provide the best customer experience<br>while creating an environment of<br>growth and opportunity for our customers,<br>employees and service providers.</p>

  <div class="brand"><span class="brand__dot"></span><span class="brand__name">KEM Logistics</span></div>
</div>
</body>
</html>
```